Redesign of 3-4 page site for professional services firm

Our site is www.kestrelvaleadvisors.com. We currently have a simple page made with HostPlumo tools. But the tools are not able to generate the look and feel we desire. We need a home page similar to current that tells a little about our company, our experience and our team. We need a second page to show details of current and past transactions we have assisted our clients with. Currently this page reads like a word document but we would like for it to present in a cleaner fashion and liven it up with some images that link to the industry served. For example, a motorcycle outline in a circle for the powersports related transactions. We would like page to introduce each member of "Our Team" and highlight their experience with a photo of each person. If there is no photo available, we would like a placeholder to be their initials in a circle that can be updated later. We would also like a contact us section whether this is a different page or part of the home page.

Target Market(s)

Retirement minded business owners

Industry/Entity Type

Professional Services

Coding

Coded - Design and coding required

Requirements
Must have
• See project description. Must include a page or section for "Current Listings" and "Recently Completed Transactions" (can be same page)

```html
<!DOCTYPE html>
<html lang="en">
<head>
<meta charset="utf-8">
<title>Kestrel Vale Advisors</title>
<link href="https://fonts.googleapis.com/css2?family=Montserrat:wght@600;700;800&family=Poppins:wght@400;500;600&display=swap" rel="stylesheet">
<style>
:root{
  --lime:#a6b51a;
  --lime-dark:#8d9a12;
  --red:#e0141e;
  --ink:#1d1d1d;
  --text:#555;
  --dark:#2b2b2b;
  --dark-2:#3a3a3a;
  --line:#e4e4e4;
  --white:#fff;
  --green:#2f8a3c;
  --teal:#1f6f5a;
}
*{box-sizing:border-box;margin:0;padding:0}
html,body{width:1200px;height:5132px;overflow:hidden}
body{font-family:'Poppins',sans-serif;color:var(--text);background:var(--white);position:relative;font-size:13px;line-height:1.6}
h1,h2,h3,h4{font-family:'Montserrat',sans-serif;color:var(--ink);text-transform:uppercase}
.abs{position:absolute}
.btn{display:inline-block;background:var(--red);color:#fff;font-weight:500;font-size:13px;padding:10px 22px;border-radius:3px}
.label{font-size:12px;font-weight:600;color:var(--lime-dark);text-transform:uppercase;letter-spacing:.5px}
.label::before{content:">> ";}
.brand{font-family:'Poppins',sans-serif;font-weight:600;font-size:24px;color:var(--ink);display:flex;align-items:center;gap:8px}
.brand i{width:14px;height:14px;background:var(--red);display:block}

/* header */
.topbar{left:0;top:0;width:1200px;height:96px;display:flex;align-items:center;justify-content:space-between;padding:0 140px}
.top-right{display:flex;align-items:center;gap:28px;font-size:12px}
.rating{display:flex;align-items:center;gap:8px}
.rating .badge{width:30px;height:30px;border-radius:50%;background:#eee}
.rating b{color:var(--ink)}
.stars{color:#f4b400;letter-spacing:1px}
.call{display:flex;align-items:center;gap:8px}
.call .ico{width:30px;height:30px;border-radius:50%;background:var(--red);display:flex;align-items:center;justify-content:center}
.btn-outline{border:1.5px solid var(--ink);padding:8px 16px;border-radius:3px;color:var(--ink);font-weight:500}
.nav{left:0;top:96px;width:1200px;height:32px;background:var(--lime);display:flex;justify-content:space-between;padding:0 140px;align-items:center}
.nav a{color:#fff;font-size:12px;font-weight:500;text-decoration:none}

/* hero */
.hero{left:0;top:128px;width:1200px;height:504px;background:
  radial-gradient(ellipse 260px 300px at 86% 60%,#2c3240 0%,rgba(44,50,64,0) 100%),
  radial-gradient(ellipse 240px 260px at 62% 55%,#c7a890 0%,rgba(199,168,144,0) 100%),
  linear-gradient(90deg,#1e1e1e 0%,#2f2f2f 35%,#8c8f94 62%,#d5d2cc 100%)}
.hero h1{position:absolute;left:140px;top:130px;color:#fff;font-size:40px;line-height:1.2;font-weight:800}
.hero p{position:absolute;left:140px;top:246px;color:#ddd;width:380px;font-size:13px}
.hero .btn{position:absolute;left:140px;top:330px}

/* about */
.about-img{left:140px;top:720px;width:420px;height:420px}
.about-img div{position:absolute;border-radius:2px}
.about-text{left:630px;top:736px;width:430px}
.about-text h2{font-size:30px;line-height:1.25;margin:8px 0 18px}
.about-text p{margin-bottom:12px;font-size:12.5px}

/* experience */
.exp-text{left:140px;top:1300px;width:430px}
.exp-text h2{font-size:30px;line-height:1.25;margin:8px 0 18px}
.exp-text p{font-size:12.5px}

/* photo band */
.band{left:0;top:1760px;width:1200px;height:440px;background:
  linear-gradient(180deg,#fff 0%,rgba(255,255,255,0) 24%,rgba(43,43,43,0) 68%,#2b2b2b 100%),
  radial-gradient(ellipse 300px 200px at 80% 62%,#262b36 0%,rgba(38,43,54,0) 100%),
  radial-gradient(ellipse 220px 160px at 60% 42%,#c9a78a 0%,rgba(201,167,138,0) 100%),
  radial-gradient(ellipse 240px 170px at 44% 70%,#3f4652 0%,rgba(63,70,82,0) 100%),
  radial-gradient(ellipse 260px 200px at 18% 50%,#f3efe8 0%,rgba(243,239,232,0) 100%),
  linear-gradient(90deg,#e6e1d9 0%,#cbc1b5 45%,#a99d90 75%,#7d746b 100%)}

/* deals */
.deals{left:0;top:2200px;width:1200px;height:600px;background:linear-gradient(180deg,#2b2b2b,#3c3c3c)}
.deals .center{position:absolute;left:140px;width:920px;text-align:center}
.deals h2{color:#fff;font-size:30px;line-height:1.25}
.deals p{color:#cfcfcf;font-size:12.5px}
.deal-card{position:absolute;top:290px;width:290px;height:170px;background:var(--dark-2);border-radius:4px;padding:24px 22px}
.deal-card .ico{width:44px;height:44px;background:var(--lime);border-radius:3px;display:flex;align-items:center;justify-content:center;margin-bottom:14px}
.deal-card h4{color:#fff;font-size:15px;text-transform:none;margin-bottom:4px}
.deal-card p{color:#cfcfcf;font-size:12px;line-height:1.5;text-align:left}
.dots{position:absolute;top:520px;left:0;width:1200px;display:flex;justify-content:center;gap:6px}
.dots i{width:8px;height:8px;border-radius:50%;background:#777;display:block}
.dots i.on{background:#fff}

/* team */
.team-head{left:140px;top:2880px;width:920px;text-align:center}
.team-head h2{font-size:30px;margin-top:8px}
.member{position:absolute;top:2990px;width:214px;height:260px;background:#fff;box-shadow:0 4px 18px rgba(0,0,0,.1);padding:10px;text-align:center}
.member .photo{height:170px;background:linear-gradient(180deg,#b9c6a0 0%,#9aa4a8 55%,#2e3440 100%)}
.member h4{text-transform:none;font-size:15px;margin-top:12px}
.member p{font-size:11px}
.rule{left:140px;top:3390px;width:920px;height:1px;background:var(--line)}

/* testimonials */
.testi-text{left:140px;top:3470px;width:360px}
.testi-text h2{font-size:30px;line-height:1.25;margin:8px 0 14px}
.testi-photo{left:560px;top:3460px;width:500px;height:260px;background:
  radial-gradient(ellipse 160px 140px at 70% 55%,#2f3540 0%,rgba(47,53,64,0) 100%),
  radial-gradient(ellipse 140px 120px at 35% 45%,#c8a88e 0%,rgba(200,168,142,0) 100%),
  linear-gradient(135deg,#eeebe6,#a29b92)}
.review{position:absolute;top:3800px;width:360px;height:230px;background:#fff;box-shadow:0 4px 18px rgba(0,0,0,.1);padding:26px}
.review .who{display:flex;gap:14px;align-items:center;margin-bottom:14px}
.review .av{width:56px;height:56px;border-radius:50%;background:linear-gradient(135deg,#d4d4d4,#8a8a8a);flex:none}
.review h4{text-transform:none;font-size:15px}
.review small{display:block;font-size:11px}
.review p{font-size:12px;line-height:1.6}

/* contact */
.footer-dark{left:0;top:4100px;width:1200px;height:520px;background:var(--dark)}
.footer-dark .brand{position:absolute;left:0;width:1200px;justify-content:center;top:60px;color:#fff;font-size:30px}
.quote{left:140px;top:4240px;width:920px;height:420px;background:var(--lime);padding:20px}
.map{position:absolute;left:20px;top:20px;width:340px;height:380px;background:linear-gradient(135deg,#e8ecef,#cfd8de)}
.form{position:absolute;left:400px;top:26px;width:500px}
.form .label{color:#1d1d1d;text-align:center;display:block}
.form h2{text-align:center;font-size:28px;margin:6px 0 20px}
.field{background:#fff;height:40px;border-radius:2px;font-size:12px;padding:10px 14px;color:#777;margin-bottom:12px}
.row{display:flex;gap:12px}.row .field{flex:1}
.field.msg{height:100px}
.form .btn{display:block;width:130px;margin:0 auto;text-align:center}

/* footer */
.cols{left:140px;top:4700px;width:920px;display:flex;justify-content:space-between}
.cols h4{text-transform:none;font-size:16px;margin-bottom:16px}
.cols li{list-style:none;display:flex;gap:10px;align-items:center;font-size:12.5px;margin-bottom:14px}
.cols .ci{width:30px;height:30px;border-radius:50%;background:var(--lime);flex:none;display:flex;align-items:center;justify-content:center}
.sub .in{width:280px;height:40px;border:1px solid var(--line);padding:10px 14px;font-size:12px;color:#888;margin-bottom:12px}
.sub .btn{width:280px;text-align:center}
.bottom{left:140px;top:5070px;width:920px;border-top:1px solid var(--line);padding-top:16px;display:flex;justify-content:space-between;font-size:11.5px}
</style>
</head>
<body>

<header class="topbar abs">
  <div class="brand"><i></i>Kestrel Vale</div>
  <div class="top-right">
    <div class="rating"><span class="badge"></span><div><b>5.0</b> <span class="stars">★★★★★</span><br>Client Rating</div></div>
    <div class="call"><span class="ico"><svg width="14" height="14" viewBox="0 0 24 24"><path fill="#fff" d="M6.6 10.8a15 15 0 006.6 6.6l2.2-2.2a1 1 0 011-.25 11.4 11.4 0 003.6.57 1 1 0 011 1V20a1 1 0 01-1 1A17 17 0 013 4a1 1 0 011-1h3.5a1 1 0 011 1c0 1.25.2 2.450.57 3.6a1 1 0 01-.25 1z"/></svg></span><div>Call Us<br><b>405-555-0148</b></div></div>
    <span class="btn-outline">Get a Free Consultation</span>
  </div>
</header>
<nav class="nav abs"><a>HOME</a><a>ABOUT US</a><a>OUR TEAM</a><a>TRANSACTIONS</a><a>CONTACT US</a></nav>

<section class="hero abs" role="img" aria-label="Business owner shaking hands with an advisor across a desk">
  <h1>Your Exit Strategy<br>Starts Here</h1>
  <p>Guiding business owners through successful transitions with experience, trust, and a proven roadmap.</p>
  <span class="btn">Explore Our Services</span>
</section>

<div class="about-img abs">
  <div role="img" aria-label="Team meeting around a table" style="left:0;top:20px;width:200px;height:380px;background:linear-gradient(160deg,#d8d2c8,#7c7468)"></div>
  <div role="img" aria-label="Advisors reviewing documents" style="left:220px;top:0;width:200px;height:250px;background:linear-gradient(160deg,#e0dcd4,#8c867c)"></div>
  <div style="left:220px;top:270px;width:200px;height:130px;background:var(--lime)"></div>
</div>
<section class="about-text abs">
  <div class="label">About Us</div>
  <h2>We Help Owners Move On The Right Way</h2>
  <p>At Kestrel Vale Advisors, our mission is to empower entrepreneurs and business owners by facilitating seamless transactions that lead to mutual success. We understand that selling or acquiring a business can be a complex and emotional journey, which is why our dedicated team of experts is here to guide you every step of the way.</p>
  <p>With a commitment to integrity, transparency, and unmatched professionalism, we strive to create a positive and rewarding experience for all our clients.</p>
  <span class="btn" style="margin-top:14px">Get a Free Consultation</span>
</section>

<section class="exp-text abs">
  <div class="label">Our Experience</div>
  <h2>Decades Of Deal<br>Making Experience</h2>
  <p>With decades of experience Kestrel Vale Advisors has proudly assisted numerous clients in successfully navigating the intricate journey of selling their businesses. Our team brings a wealth of knowledge and expertise acquired through years of working closely with entrepreneurs and business owners across diverse industries. We understand the unique challenges and complexities involved in selling a business, from valuation and marketing to negotiations and closing the deal. Our extensive experience allows us to anticipate potential obstacles and proactively find solutions, ensuring a seamless and efficient process for our clients.</p>
</section>
<svg class="abs" style="left:640px;top:1390px" width="420" height="190" viewBox="0 0 420 190">
  <rect x="0" y="120" width="130" height="60" fill="#2f8a3c"/>
  <text x="65" y="147" fill="#fff" font-family="Poppins,sans-serif" font-size="12" text-anchor="middle">Proven Track</text>
  <text x="65" y="163" fill="#fff" font-family="Poppins,sans-serif" font-size="12" text-anchor="middle">Record</text>
  <rect x="110" y="66" width="130" height="60" fill="#3d9c4a"/>
  <text x="175" y="93" fill="#fff" font-family="Poppins,sans-serif" font-size="12" text-anchor="middle">Deep Industry</text>
  <text x="175" y="109" fill="#fff" font-family="Poppins,sans-serif" font-size="12" text-anchor="middle">Knowledge</text>
  <path d="M220 10h150v-10l50 40-50 40v-10H220z" fill="#1f6f5a"/>
  <text x="300" y="38" fill="#fff" font-family="Poppins,sans-serif" font-size="12" text-anchor="middle">End-to-End</text>
  <text x="300" y="54" fill="#fff" font-family="Poppins,sans-serif" font-size="12" text-anchor="middle">Transaction Support</text>
</svg>

<div class="band abs" role="img" aria-label="Advisors and client in suits discussing a deal at a laptop in a bright office"></div>

<section class="deals abs">
  <div class="center" style="top:44px"><div class="label">Successful Transactions</div></div>
  <div class="center" style="top:72px"><h2>A Glimpse At Recent Deals We've Helped<br>Bring To Life</h2></div>
  <div class="center" style="top:164px;padding:0 40px"><p>We've helped business owners across a wide range of industries achieve successful exits—from powersports and logistics to retail and beyond. Each transaction represents a story of strategic planning, expert negotiation, and a commitment to getting the best outcome for our clients. Below is a preview of just a few of the businesses we've guided through their transition.</p></div>
  <div class="deal-card" style="left:140px"><div class="ico"><svg width="24" height="24" viewBox="0 0 24 24" fill="none" stroke="#fff" stroke-width="2"><circle cx="5" cy="16" r="3"/><circle cx="19" cy="16" r="3"/><path d="M5 16l5-6h5l4 6M12 10l-2-3h-2"/></svg></div><h4>Powersports</h4><p>Sold Multi-Location Dealer<br>to National Brand</p></div>
  <div class="deal-card" style="left:455px"><div class="ico"><svg width="24" height="24" viewBox="0 0 24 24" fill="none" stroke="#fff" stroke-width="2"><rect x="2" y="7" width="12" height="9"/><path d="M14 10h4l3 3v3h-7"/><circle cx="6" cy="18" r="2"/><circle cx="17" cy="18" r="2"/></svg></div><h4>Logistics Firm</h4><p>Managed Exit to Investor<br>Group with Stakeholder Buy-In</p></div>
  <div class="deal-card" style="left:770px"><div class="ico"><svg width="24" height="24" viewBox="0 0 24 24" fill="none" stroke="#fff" stroke-width="2"><path d="M3 9l2-5h14l2 5M4 9v11h16V9M3 9h18M10 20v-6h4v6"/></svg></div><h4>Retail Chain</h4><p>Guided 3-Store Sale to<br>Equity Group</p></div>
  <div class="dots"><i class="on"></i><i></i><i></i><i></i></div>
</section>

<section class="team-head abs">
  <div class="label">Meet Our Team</div>
  <h2>Meet The People Who Power Your Plan</h2>
</section>
<div class="member" style="left:140px"><div class="photo" role="img" aria-label="Portrait of Owen Hartley"></div><h4>Owen Hartley</h4><p>Owen is a founding broker...</p></div>
<div class="member" style="left:375px"><div class="photo" role="img" aria-label="Portrait of Miles Crandall"></div><h4>Miles Crandall</h4><p>Miles has more than 20 years...</p></div>
<div class="member" style="left:610px"><div class="photo" role="img" aria-label="Portrait of Reid Lawson"></div><h4>Reid Lawson</h4><p>Reid is a sales &amp; marketing...</p></div>
<div class="member" style="left:846px"><div class="photo" role="img" aria-label="Portrait of Walter Ames"></div><h4>Walter Ames</h4><p>Walter has over 30 years...</p></div>
<div class="rule abs"></div>

<section class="testi-text abs">
  <div class="label">Client Testimonials</div>
  <h2>Trusted By Those<br>We've Helped</h2>
  <p>See how we've made a difference in the lives of our clients.</p>
</section>
<div class="testi-photo abs" role="img" aria-label="Smiling client meeting with an advisor"></div>

<div class="review" style="left:-240px"><div class="who"><span class="av"></span><div><h4>Client</h4><small>Retailer</small><span class="stars">★★★★★</span></div></div><p>They took the time to understand our goals and guided us through every step of the sale with care.</p></div>
<div class="review" style="left:180px"><div class="who"><span class="av"></span><div><h4>Nora Pellman</h4><small>Retailer</small><span class="stars">★★★★★</span></div></div><p>Selling our family shop felt daunting until we met this team. They kept us informed, found the right buyer and made the closing smooth. We could not have asked for better partners.</p></div>
<div class="review" style="left:600px"><div class="who"><span class="av"></span><div><h4>Greta Holloway</h4><small>Retailer</small><span class="stars">★★★★★</span></div></div><p>From valuation to final signature, every detail was handled with patience and skill. Our exit went better than we hoped and we felt supported the whole way.</p></div>
<div class="review" style="left:1020px"><div class="who"><span class="av"></span><div><h4>Lucy Brandt</h4><small>Retailer</small><span class="stars">★★★★★</span></div></div><p>Honest advice and steady guidance made our transition simple and stress free.</p></div>

<section class="footer-dark abs"><div class="brand"><i></i>Kestrel Vale</div></section>
<section class="quote abs">
  <div class="map" role="img" aria-label="Map showing the office location"></div>
  <div class="form">
    <span class="label">Request a Quote</span>
    <h2>Get In Touch With Us</h2>
    <div class="field">First Name*</div>
    <div class="row"><div class="field">Email Address*</div><div class="field">Phone Number*</div></div>
    <div class="field msg">Message</div>
    <span class="btn">Submit Now</span>
  </div>
</section>

<footer class="cols abs">
  <div>
    <h4>Contact Us</h4>
    <ul>
      <li><span class="ci"><svg width="14" height="14" viewBox="0 0 24 24"><path fill="#fff" d="M12 2a7 7 0 00-7 7c0 5 7 13 7 13s7-8 7-13a7 7 0 00-7-7zm0 9.5A2.5 2.5 0 1112 6a2.5 2.5 0 010 5.5z"/></svg></span>48 Larkspur Road, Fairbank,<br>Oklahoma 74010 United States</li>
      <li><span class="ci"><svg width="14" height="14" viewBox="0 0 24 24" fill="none" stroke="#fff" stroke-width="2"><rect x="3" y="5" width="18" height="14"/><path d="M3 6l9 7 9-7"/></svg></span>info@kestrelvaleadvisors.com</li>
      <li><span class="ci"><svg width="14" height="14" viewBox="0 0 24 24"><path fill="#fff" d="M6.6 10.8a15 15 0 006.6 6.6l2.2-2.2a1 1 0 011-.25 11.4 11.4 0 003.6.57 1 1 0 011 1V20a1 1 0 01-1 1A17 17 0 013 4a1 1 0 011-1h3.5a1 1 0 011 1c0 1.25.2 2.45.57 3.6a1 1 0 01-.25 1z"/></svg></span>405-555-0148</li>
    </ul>
  </div>
  <div>
    <h4>Quick Links</h4>
    <ul><li>Home</li><li>Transactions</li><li>Our Team</li><li>Contact us</li></ul>
  </div>
  <div class="sub">
    <h4>Subscribe to Our Newsletter</h4>
    <div class="in">Your email address</div>
    <span class="btn">Subscribe Now</span>
  </div>
</footer>
<div class="bottom abs"><span>Copyright ©2025 Kestrel Vale Advisors Professional Services | All Rights Reserved</span><span>Terms &amp; Conditions &nbsp;&nbsp;&nbsp; Privacy Policy</span></div>

</body>
</html>
```